Architectural firm needs a graphic representation of our Master Planning process

We need an image to convey our 3-phase, 8-step Master Planning process that we utilize when designing plans for schools K-12. What we currently use looks very outdated in both the design and color scheme. We'd like an EPS created that can be scaled without distortion. The files I've attached show the current graphic and an instruction sheet which also contains our colors.

```html
<!DOCTYPE html>
<html lang="en">
<head>
<meta charset="utf-8">
<title>Master Planning Process</title>
<link rel="stylesheet" href="https://fonts.googleapis.com/css2?family=Arimo:wght@700&display=swap">
<style>
  :root {
    --rose: #dfa69d;
    --rose-deep: #cd958c;
    --lavender: #a7a6cd;
    --lavender-deep: #9796bf;
    --lime: #b9da5b;
    --lime-deep: #a9c94f;
    --tread: #6e6f72;
    --ink: #231f20;
    --building: #a8a7cd;
    --paper: #ffffff;
  }
  html, body {
    margin: 0;
    padding: 0;
    width: 1200px;
    height: 922px;
    overflow: hidden;
    background: var(--paper);
  }
  .process-graphic {
    display: block;
    width: 1200px;
    height: 922px;
  }
  .tread { fill: var(--tread); }
  .riser-rose { fill: url(#rose-fade); }
  .riser-lavender { fill: url(#lavender-fade); }
  .riser-lime { fill: url(#lime-fade); }
  .step-label {
    font-family: "Arimo", Arial, sans-serif;
    font-weight: 700;
    fill: var(--ink);
    text-anchor: middle;
  }
  .label-small { font-size: 25px; }
  .label-medium { font-size: 38px; }
  .label-wide { font-size: 44px; letter-spacing: 20px; }
  .label-vision { font-size: 50px; letter-spacing: 24px; }
</style>
</head>
<body>
<svg class="process-graphic" viewBox="0 0 1500 1152.5" xmlns="http://www.w3.org/2000/svg">
  <defs>
    <linearGradient id="rose-fade" x1="0" y1="0" x2="0" y2="1">
      <stop offset="0" stop-color="var(--rose)"/>
      <stop offset="1" stop-color="var(--rose-deep)"/>
    </linearGradient>
    <linearGradient id="lavender-fade" x1="0" y1="0" x2="0" y2="1">
      <stop offset="0" stop-color="var(--lavender)"/>
      <stop offset="1" stop-color="var(--lavender-deep)"/>
    </linearGradient>
    <linearGradient id="lime-fade" x1="0" y1="0" x2="0" y2="1">
      <stop offset="0" stop-color="var(--lime)"/>
      <stop offset="1" stop-color="var(--lime-deep)"/>
    </linearGradient>
  </defs>

  <!-- School building -->
  <rect class="school-building" x="498" y="133" width="515" height="316" rx="4" fill="var(--building)"
        role="img" aria-label="Illustration of a school building with a central gabled entrance and a SCHOOL sign"/>

  <!-- Step 1 -->
  <polygon class="tread" points="498,448 1013,448 1037,456 474,456"/>
  <rect class="riser-rose" x="474" y="455" width="281" height="63"/>
  <rect class="riser-lime" x="755" y="455" width="282" height="63"/>
  <text class="step-label label-small" x="635" y="484">ARCHITECTURAL</text>
  <text class="step-label label-small" x="635" y="509">CONSULTANT</text>
  <text class="step-label label-small" x="891" y="484">FUND RAISING</text>
  <text class="step-label label-small" x="891" y="509">CONSULTANT</text>

  <!-- Step 2 -->
  <polygon class="tread" points="474,518 1037,518 1067,527 444,527"/>
  <rect class="riser-rose" x="444" y="527" width="207" height="63"/>
  <rect class="riser-lavender" x="651" y="527" width="209" height="63"/>
  <rect class="riser-lime" x="860" y="527" width="207" height="63"/>
  <text class="step-label label-vision" x="769" y="576">VISIONING</text>

  <!-- Step 3 -->
  <polygon class="tread" points="444,590 1067,590 1101,598 407,598"/>
  <rect class="riser-rose" x="407" y="598" width="347" height="63"/>
  <rect class="riser-lime" x="754" y="598" width="347" height="63"/>
  <text class="step-label label-small" x="585" y="625">PHYSICAL CONDITIONS</text>
  <text class="step-label label-small" x="585" y="654">ASSESSMENT</text>
  <text class="step-label label-small" x="933" y="625">SPACE NEEDS</text>
  <text class="step-label label-small" x="933" y="654">ASSESSMENT</text>

  <!-- Step 4 -->
  <polygon class="tread" points="407,661 1101,661 1138,669 370,669"/>
  <rect class="riser-rose" x="370" y="669" width="768" height="64"/>
  <text class="step-label label-medium" x="752" y="716">PROBLEM DEFINED</text>

  <!-- Step 5 -->
  <polygon class="tread" points="370,733 1138,733 1179,741 325,741"/>
  <rect class="riser-rose" x="325" y="741" width="854" height="64"/>
  <text class="step-label label-medium" x="752" y="789">IDENTIFY SOLUTIONS</text>

  <!-- Step 6 -->
  <polygon class="tread" points="325,805 1179,805 1225,813 279,813"/>
  <rect class="riser-rose" x="279" y="813" width="316" height="63"/>
  <rect class="riser-lavender" x="595" y="813" width="315" height="63"/>
  <rect class="riser-lime" x="910" y="813" width="315" height="63"/>
  <text class="step-label label-medium" x="752" y="862">ASSESS &amp; SELECT</text>

  <!-- Step 7 -->
  <polygon class="tread" points="279,876 1225,876 1276,885 224,885"/>
  <rect class="riser-rose" x="224" y="885" width="1052" height="63"/>
  <text class="step-label label-medium" x="752" y="933">COMPILE REPORT</text>

  <!-- Step 8 -->
  <polygon class="tread" points="224,948 1276,948 1332,956 167,956"/>
  <rect class="riser-rose" x="167" y="956" width="389" height="63"/>
  <rect class="riser-lavender" x="556" y="956" width="388" height="63"/>
  <rect class="riser-lime" x="944" y="956" width="388" height="63"/>
  <text class="step-label label-wide" x="760" y="1005">IMPLEMENT PLAN</text>
</svg>
</body>
</html>
```